THE PRACTICE NAME "The Corvane MD" FOR A NEW MEDICAL PRACTICE STARTUP

THIS IS A BUSINESS CARD REQUEST FOR A KIDNEY DOCTOR's(NEPHROLOGIST) PRACTICE, THIS PRACTICE WILL BE IN EL PASO,TEXAS USA.OPEN TO INNOVATIVE IDEAS!

THE CORVANE MD ( NAME OF PRACTICE)

DEVESH R. MALHOTRA, MD FNKF FASN ( NAME OF PHYSICIAN WITH DEGREES)
BOARD CERTIFIED INTERNAL MEDICINE
BOARD CERTIFIED NEPHROLOGY
HYPERTENSION SPECIALIST

OFFICE ADDRESS, PHONE, FAX AND EMAIL PENDING

Saving Kidneys. Saving Lives.(MOTTO) THE LOGO SHOILD REFLECT THIS MESSAGE. WE NEED A LOGO DESIGN WITH 2 KIDNEYS OR CAN BE ONE KIDNEY ALSO.

Target Market(s)

PATIENTS WITH KIDNEY DISEASE, HYPERTENSION, ENGLISH AND SPANISH SPEAKING POPULATION AND PATIENTS ON DIALYSIS

Industry/Entity Type

Health Care

Contact Information for Business Card

HYPERTENSION SPECIALIST

WEBSITE URL PENDING

Font styles to use
Serif
Sans Serif
Script

Colors
fbed38
ffc214
fbf289
fbee3e
5c5c5c
333333
1b1b1b
757575
d3d3d3

Requirements
Must have
• A KIDNEY LOGO
• NAME OF THE PRACTICE
Nice to have
• IF THE CARD CAN BE IN THE SHAPE OF A KIDNEY

```html
<!DOCTYPE html>
<html lang="en">
<head>
<meta charset="utf-8">
<title>The Corvane MD – Business Cards</title>
<link rel="stylesheet" href="https://fonts.googleapis.com/css2?family=Josefin+Sans:wght@400;600;700&display=swap">
<style>
  :root {
    --backdrop: #dedede;
    --card-yellow: #f3ea1f;
    --card-black: #1b1b1b;
    --pattern-black: #222222;
    --ink-dark: #1b1b1b;
    --ink-yellow: #f3ea1f;
  }
  * { margin: 0; padding: 0; box-sizing: border-box; }
  html, body {
    width: 1200px; height: 900px; overflow: hidden;
    background: var(--backdrop);
    font-family: "Josefin Sans", Arial, sans-serif;
  }
  .canvas { position: relative; width: 1200px; height: 900px; }
  .card { position: absolute; width: 560px; height: 390px; }
  .card-shape { position: absolute; inset: 0; width: 100%; height: 100%; }
  .card-front { left: 40px; top: 440px; }
  .card-back { left: 600px; top: 90px; }

  .brand {
    position: absolute;
    font-weight: 700;
    text-transform: uppercase;
    letter-spacing: -0.01em;
    line-height: 0.9;
    text-align: center;
  }
  .brand .brand-small { display: block; font-size: 0.5em; text-align: left; }

  .card-front .brand {
    color: var(--ink-dark);
    font-size: 38px;
    left: 0; right: 0; top: 118px;
  }
  .card-front .brand span { display: inline-block; }

  .physician {
    position: absolute; left: 0; right: 0; top: 185px;
    text-align: center; color: var(--ink-dark);
  }
  .physician-name { font-size: 20px; font-weight: 400; letter-spacing: 0.01em; }
  .physician-name .credentials { font-size: 15px; }
  .specialty { font-size: 13px; margin-top: 6px; letter-spacing: 0.01em; }

  .contact {
    position: absolute; left: 90px; top: 275px;
    font-size: 14px; color: var(--ink-dark); line-height: 1.6;
  }
  .contact-row { display: flex; align-items: center; gap: 6px; }
  .contact-row svg { width: 13px; height: 13px; fill: var(--ink-dark); }
  .divider { margin: 0 8px; }

  .card-back .brand {
    color: var(--ink-yellow);
    font-size: 56px;
    left: 0; right: 0; top: 130px;
  }
  .card-back .brand span { display: inline-block; }
  .website {
    position: absolute; left: 0; right: 0; top: 255px;
    text-align: center; font-size: 16px; color: var(--ink-yellow);
  }
</style>
</head>
<body>
<main class="canvas">

  <section class="card card-front">
    <svg class="card-shape" viewBox="0 0 560 390" aria-hidden="true">
      <path fill="var(--card-yellow)" d="M20 210 C20 85 125 25 235 35 C300 42 315 105 375 105 C440 105 460 55 510 85 C560 115 555 225 515 295 C470 370 340 385 235 380 C100 373 20 330 20 210 Z"/>
    </svg>
    <div class="brand"><span><span class="brand-small">The</span>Corvane MD</span></div>
    <div class="physician">
      <p class="physician-name">DEVESH R. MALHOTRA, <span class="credentials">MD FNKF FASN</span></p>
      <p class="specialty">BOARD CERTIFIED INTERNAL MEDICINE</p>
      <p class="specialty">BOARD CERTIFIED NEPHROLOGY &nbsp;|&nbsp; HYPERTENSION SPECIALIST</p>
    </div>
    <div class="contact">
      <p class="contact-row">
        <svg viewBox="0 0 24 24"><path d="M6.6 10.8a15 15 0 0 0 6.6 6.6l2.2-2.2a1 1 0 0 1 1-.25 11.4 11.4 0 0 0 3.6.57 1 1 0 0 1 1 1V20a1 1 0 0 1-1 1A17 17 0 0 1 3 4a1 1 0 0 1 1-1h3.5a1 1 0 0 1 1 1c0 1.25.2 2.45.57 3.6a1 1 0 0 1-.25 1z"/></svg>
        000 000 0000<span class="divider">|</span>
        <svg viewBox="0 0 24 24"><path d="M2 5h20v14H2z M2 5l10 8 10-8" /></svg>
        youremail@xyz.com
      </p>
      <p class="contact-row">
        <svg viewBox="0 0 24 24"><path d="M12 2a7 7 0 0 0-7 7c0 5 7 13 7 13s7-8 7-13a7 7 0 0 0-7-7zm0 9.5A2.5 2.5 0 1 1 12 6.5a2.5 2.5 0 0 1 0 5z"/></svg>
        000, Street name, Anywhere, ST 0000
      </p>
    </div>
  </section>

  <section class="card card-back">
    <svg class="card-shape" viewBox="0 0 560 390">
      <path fill="var(--card-black)" d="M20 210 C20 85 125 25 235 35 C300 42 315 105 375 105 C440 105 460 55 510 85 C560 115 555 225 515 295 C470 370 340 385 235 380 C100 373 20 330 20 210 Z"/>
      <path role="img" aria-label="Faint repeating kidney pattern across the card" fill="var(--pattern-black)" opacity="0.6" d="M20 210 C20 85 125 25 235 35 C300 42 315 105 375 105 C440 105 460 55 510 85 C560 115 555 225 515 295 C470 370 340 385 235 380 C100 373 20 330 20 210 Z"/>
    </svg>
    <div class="brand"><span><span class="brand-small">The</span>Corvane MD</span></div>
    <p class="website">www.yourwebsite.com</p>
  </section>

</main>
</body>
</html>
```